Design a flyer to be given to attendees of a STEM teacher conference.

Design a flyer for Harbel Instruments' 3D-printing consumables.

Target Market(s)

Education, Technology

Industry/Entity Type

Technology

Colors
00AB8E
00BBA5
67D7C9
C6EFE9
E9F9F6

Requirements
Must have
• The key points in the pdf file. Our logo.
Nice to have
• Some product picture from our website www.harbelinst.com.au

```html
<!DOCTYPE html>
<html lang="en">
<head>
<meta charset="utf-8">
<title>Harbel Instruments – STEM Filaments Flyer</title>
<link rel="stylesheet" href="https://fonts.googleapis.com/css2?family=Poppins:wght@300;400;500;600;700;800&display=swap">
<style>
  :root {
    --teal: #2BAA8C;
    --teal-deep: #00AB8E;
    --teal-light: #C6EFE9;
    --mint-bg: #EAF7F5;
    --ink: #111111;
    --white: #FFFFFF;
  }
  * { margin: 0; padding: 0; box-sizing: border-box; }
  html, body { width: 872px; height: 1200px; overflow: hidden; background: var(--mint-bg); }
  .flyer {
    position: relative; width: 872px; height: 1200px; overflow: hidden;
    background: var(--mint-bg);
    font-family: "Poppins", sans-serif; color: var(--ink);
  }
  .abs { position: absolute; }
  .rays { left: 0; top: 0; }
  .green-field { left: 0; top: 0; }

  .brand { left: 39px; top: 48px; display: flex; align-items: center; gap: 16px; }
  .brand-square { width: 58px; height: 58px; background: var(--teal); border-radius: 6px; }
  .brand-name { font-weight: 700; font-size: 30px; line-height: 1; color: var(--ink); letter-spacing: 1px; }

  .headline { left: 45px; top: 206px; font-size: 47px; line-height: 50px; letter-spacing: -0.5px; }
  .headline .strong { font-weight: 800; display: block; }
  .headline .light { font-weight: 300; display: block; }
  .headline-band {
    left: 45px; top: 312px; width: 598px; height: 58px;
    background: var(--teal);
    border-radius: 0 6px 6px 0;
    clip-path: polygon(0 0, 98% 0, 100% 100%, 0 100%);
    color: var(--white); font-weight: 500; font-size: 38px; letter-spacing: 16px;
    display: flex; align-items: center; justify-content: center; padding-left: 16px;
  }

  .subhead { left: 45px; top: 410px; font-size: 26px; line-height: 30px; font-weight: 600; }
  .subhead .accent { color: var(--teal); display: block; }

  .feature-icon { width: 76px; height: 76px; border-radius: 50%; background: var(--teal); display: flex; align-items: center; justify-content: center; }
  .feature-icon.shield { left: 44px; top: 476px; }
  .feature-icon.leaf { left: 44px; top: 579px; }
  .feature-divider { left: 133px; top: 470px; height: 188px; border-left: 1.5px dashed var(--teal); }
  .feature { left: 154px; width: 300px; font-size: 16px; line-height: 20px; font-weight: 400; }
  .feature h3 { font-size: 15.5px; font-weight: 700; line-height: 20px; margin-bottom: 1px; }
  .feature.durable { top: 470px; }
  .feature.eco { top: 573px; }

  .product-photo {
    left: 542px; top: 440px; width: 330px; height: 440px;
    background: linear-gradient(160deg, #3a3d42 0%, #1c1e21 55%, #2a2c30 100%);
    border-radius: 4px 0 0 0;
  }
  .spools-photo {
    left: 526px; top: 800px; width: 346px; height: 160px;
    background: linear-gradient(90deg, #c9a07a 0%, #b857c9 35%, #7a5bd6 50%, #d4b46a 70%, #2f8f9a 100%);
    border-radius: 80px 0 0 80px;
  }

  .why-pill {
    left: 45px; top: 684px; width: 497px; height: 112px;
    background: var(--white); border-radius: 56px 0 0 56px;
  }
  .why-title { left: 97px; top: 704px; font-size: 29px; line-height: 34px; font-weight: 700; color: var(--teal); }

  .checklist { left: 61px; top: 814px; width: 460px; list-style: none; color: var(--white); }
  .checklist li { position: relative; padding-left: 30px; font-size: 16px; line-height: 22px; margin-bottom: 8px; font-weight: 400; }
  .checklist li strong { font-weight: 700; }
  .checklist svg { position: absolute; left: 0; top: 3px; }

  .offer { left: 61px; top: 982px; color: var(--white); font-weight: 800; font-size: 31px; line-height: 35px; }
  .offer-divider { left: 473px; top: 986px; height: 64px; border-left: 1.5px dashed var(--white); opacity: 0.85; }
  .discount { left: 489px; top: 982px; color: var(--white); font-weight: 800; font-size: 31px; line-height: 35px; }
  .code-note { left: 564px; top: 984px; color: var(--white); font-weight: 500; font-size: 19px; line-height: 24px; }
  .code-pill { background: var(--teal-light); color: var(--teal-deep); border-radius: 8px; padding: 0 7px; }

  .contact { left: 58px; top: 1074px; color: var(--white); }
  .contact .label { font-size: 21px; font-weight: 500; line-height: 26px; }
  .contact .phone { font-size: 46px; font-weight: 800; line-height: 50px; letter-spacing: -0.5px; }
  .contact .email { font-size: 18px; font-weight: 400; line-height: 24px; }
  .website { right: 43px; top: 1155px; color: var(--white); font-size: 16px; font-weight: 600; }
</style>
</head>
<body>
<main class="flyer">
  <svg class="abs rays" width="872" height="1200" aria-hidden="true">
    <g stroke="#FFFFFF" stroke-width="10" opacity="0.55">
      <line x1="420" y1="130" x2="580" y2="0"/>
      <line x1="420" y1="210" x2="720" y2="0"/>
      <line x1="700" y1="150" x2="872" y2="40"/>
      <line x1="780" y1="420" x2="872" y2="260"/>
    </g>
  </svg>

  <svg class="abs green-field" width="872" height="1200" aria-hidden="true">
    <polygon points="0,713 542,684 872,660 872,1200 0,1200" fill="var(--teal)"/>
  </svg>

  <header class="abs brand">
    <span class="brand-square"></span>
    <span class="brand-name">HARBEL<br>INSTRUMENTS</span>
  </header>

  <h1 class="abs headline">
    <span class="strong">UNLOCK THE FUTURE OF</span>
    <span class="light">3D PRINTING WITH HARBEL</span>
  </h1>
  <div class="abs headline-band">INSTRUMENTS</div>

  <h2 class="abs subhead">HIGH-QUALITY FILAMENTS<span class="accent">FOR STEM EDUCATION</span></h2>

  <div class="abs feature-icon shield">
    <svg width="44" height="44" viewBox="0 0 44 44" fill="none" stroke="#fff" stroke-width="3" stroke-linejoin="round">
      <path d="M22 4 L38 10 V22 C38 31 31 37 22 40 C13 37 6 31 6 22 V10 Z"/>
      <path d="M22 10 L32 14 V22 C32 28 28 32 22 34 C16 32 12 28 12 22 V14 Z"/>
    </svg>
  </div>
  <div class="abs feature-icon leaf">
    <svg width="46" height="46" viewBox="0 0 46 46" fill="#fff">
      <path d="M23 6 C30 12 30 22 23 30 C16 22 16 12 23 6 Z"/>
      <path d="M4 24 C13 21 20 25 23 33 C15 35 8 31 4 24 Z"/>
      <path d="M42 24 C33 21 26 25 23 33 C31 35 38 31 42 24 Z"/>
      <rect x="10" y="36" width="26" height="2.5" rx="1"/>
    </svg>
  </div>
  <div class="abs feature-divider"></div>

  <section class="abs feature durable">
    <h3>Durable and Reliable:</h3>
    <p>Our filaments ensure consistent, high-quality prints every time ideal for classroom projects.</p>
  </section>
  <section class="abs feature eco">
    <h3>Eco-Friendly Options:</h3>
    <p>Choose from our range of Sustainable materials, helping schools meet green initiatives.</p>
  </section>

  <div class="abs product-photo" role="img" aria-label="Black enclosed 3D printer with glass doors"></div>

  <div class="abs why-pill"></div>
  <h2 class="abs why-title">WHY HARBEL INSTRUMENTS<br>FILAMENTS?</h2>

  <div class="abs spools-photo" role="img" aria-label="Spools of silk 3D printer filament in copper, purple, gold and teal with a printed dragon model"></div>

  <ul class="abs checklist">
    <li><svg width="18" height="18" viewBox="0 0 18 18" fill="none" stroke="#fff" stroke-width="2" stroke-linecap="round" stroke-linejoin="round"><path d="M14 9 V15 H3 V4 H11"/><path d="M6 8 L9 11 L16 3"/></svg><strong>Aesthetic Filaments:</strong> Perfect for eye-catching, professional looking classroom models.</li>
    <li><svg width="18" height="18" viewBox="0 0 18 18" fill="none" stroke="#fff" stroke-width="2" stroke-linecap="round" stroke-linejoin="round"><path d="M14 9 V15 H3 V4 H11"/><path d="M6 8 L9 11 L16 3"/></svg><strong>Reliable &amp; Durable:</strong> Consistent prints for hands-on STEM projects.</li>
    <li><svg width="18" height="18" viewBox="0 0 18 18" fill="none" stroke="#fff" stroke-width="2" stroke-linecap="round" stroke-linejoin="round"><path d="M14 9 V15 H3 V4 H11"/><path d="M6 8 L9 11 L16 3"/></svg><strong>Eco-Friendly Options:</strong> Choose sustainable materials for a greener classroom.</li>
  </ul>

  <p class="abs offer">EXCLUSIVE OFFER FOR<br>FORUM ATTENDEES</p>
  <div class="abs offer-divider"></div>
  <p class="abs discount">10%<br>OFF</p>
  <p class="abs code-note">WITH CODE<br><span class="code-pill">QUANTUM</span> ON<br>YOUR FIRST ORDER!</p>

  <address class="abs contact" style="font-style: normal;">
    <p class="label">GET IN TOUCH!</p>
    <p class="phone">03 9412 6630</p>
    <p class="email">sales@harbelinst.com.au</p>
  </address>
  <p class="abs website">www.harbelinst.com.au</p>
</main>
</body>
</html>
```